Brovana Landing Web Page

We need a web design for a new company head quartered in Philadelphia, PA with satellite offices in San Francisco, CA and New York, NY.
We have a logo and can provide the logo image file.
Here is some information on who we are:
Brovana
Growing information technology companies with experience
About Us: Brovana is an information technology incubator. We cultivate and groom start-ups from concept to reality to profitability. Brovana is managed and owned by entrepreneurs and technologists with proven start-up success. We seek to leverage synergies between our companies which foster innovation, stimulate creativity, increase productivity, streamline operational processes, and facilitate opportunity.
Brovana Companies:
• Brovana Health (should hyperlink to Brovana Health About Us section)
• Brovana IT Services and Staffing (should hyperlink to Brovana IT Services and Staffing About Us section)
Target Market(s)
Healthcare
Industry/Entity Type
Information Technology
Look and feel

```html
<!DOCTYPE html>
<html lang="en">
<head>
<meta charset="utf-8">
<title>Brovana Landing Web Page</title>
<link href="https://fonts.googleapis.com/css2?family=PT+Sans:wght@400;700&family=Questrial&display=swap" rel="stylesheet">
<style>
  :root {
    --brand: #2aafd9;
    --brand-dark: #136fa6;
    --band-top: #0a5a94;
    --band-bottom: #2b93cb;
    --heading: #1a6fa8;
    --link: #1b7fc1;
    --body-text: #4a4a4a;
    --rule: #dfe3e6;
    --nav-top: #f3f9fd;
    --nav-bottom: #d3e8f6;
    --nav-border: #b7d6ec;
    --button: #2a8fcc;
    --button-dark: #1a6fad;
    --footer: #0c5f98;
    --white: #ffffff;
    --green: #5cb82c;
  }
  * { box-sizing: border-box; margin: 0; padding: 0; }
  html, body { width: 1182px; height: 1200px; overflow: hidden; }
  body {
    position: relative;
    background: var(--white);
    font-family: "PT Sans", Arial, sans-serif;
    color: var(--body-text);
  }
  a { text-decoration: none; color: inherit; }

  .top-strip { position: absolute; left: 0; top: 0; width: 1182px; height: 9px; background: #e6e6e6; }

  .brand { position: absolute; left: 42px; top: 50px; display: flex; align-items: center; gap: 12px; }
  .brand-mark { width: 66px; height: 66px; border-radius: 50%; background: var(--brand-dark); }
  .brand-name { font-family: "PT Sans", Arial, sans-serif; font-size: 46px; font-weight: 400; color: var(--brand); letter-spacing: 0.5px; }

  .contact-bar { position: absolute; left: 976px; top: 36px; display: flex; align-items: center; gap: 6px; }
  .contact-bar span { font-size: 14px; color: var(--heading); margin-right: 4px; }
  .social-box { width: 22px; height: 22px; border-radius: 4px; background: var(--button); }

  .main-nav {
    position: absolute; left: 418px; top: 102px; width: 734px; height: 50px;
    display: flex; border: 1px solid var(--nav-border); border-radius: 6px;
    background: linear-gradient(var(--nav-top), var(--nav-bottom));
  }
  .main-nav a {
    display: flex; align-items: center; justify-content: center;
    font-size: 17px; color: var(--heading); border-right: 1px solid var(--nav-border);
  }
  .main-nav a:last-child { border-right: none; }

  .hero-band {
    position: absolute; left: 0; top: 174px; width: 1182px; height: 428px;
    background: linear-gradient(var(--band-top), var(--band-bottom));
  }
  .slider {
    position: absolute; left: 30px; top: 209px; width: 1117px; height: 358px;
    border-radius: 6px; overflow: hidden;
    background: linear-gradient(160deg, #ffffff 40%, #e4f3fb 70%, #9fd6f1 100%);
    box-shadow: 0 2px 8px rgba(0,0,0,0.25);
  }
  .slider-photo {
    position: absolute; left: 0; top: 0; width: 520px; height: 358px;
    background: radial-gradient(ellipse at 55% 45%, #dfe8ee 0%, #f4f7f9 45%, #ffffff 75%);
  }
  .slider-copy { position: absolute; left: 616px; top: 76px; width: 460px; }
  .slider-title { font-family: "Questrial", sans-serif; font-size: 30px; color: var(--heading); font-weight: 400; border-bottom: 1px solid #8cc6e6; display: inline-block; padding-bottom: 1px; }
  .slider-subline { font-family: "Questrial", sans-serif; font-size: 17px; color: var(--heading); margin-top: 6px; letter-spacing: 0.2px; white-space: nowrap; }
  .slider-text { font-size: 14px; line-height: 22px; color: var(--link); margin-top: 12px; width: 440px; }
  .slider-actions { display: flex; gap: 5px; margin-top: 20px; }
  .btn {
    height: 33px; padding: 0 11px; display: flex; align-items: center; justify-content: center;
    white-space: nowrap;
    font-family: "Questrial", sans-serif; font-size: 14.5px; color: var(--white);
    background: linear-gradient(var(--button), var(--button-dark));
    border: 1px solid #125f94; border-radius: 2px;
  }
  .btn-read { width: 123px; }
  .btn-services { width: 182px; }
  .slider-arrow {
    position: absolute; top: 366px; width: 22px; height: 40px; background: var(--white);
    border-radius: 4px; display: flex; align-items: center; justify-content: center;
  }
  .slider-arrow.prev { left: 9px; }
  .slider-arrow.next { left: 1148px; }

  .services {
    position: absolute; left: 28px; top: 585px; width: 1121px; height: 190px;
    background: var(--white);
  }
  .service { position: absolute; top: 15px; width: 260px; }
  .service-head { display: flex; align-items: center; gap: 10px; height: 44px; }
  .service-head h3 { font-size: 21px; font-weight: 400; color: var(--heading); white-space: nowrap; }
  .service p { font-size: 13px; line-height: 18.5px; color: var(--link); margin-top: 16px; width: 236px; }
  .service .more { display: block; font-size: 14px; color: var(--link); margin-top: 10px; }
  .service .more b { color: var(--heading); }
  .service-divider { position: absolute; top: 18px; width: 1px; height: 155px; background: var(--rule); }

  .section-rule { position: absolute; left: 35px; top: 795px; width: 1124px; height: 1px; background: var(--rule); }

  .about { position: absolute; left: 38px; top: 818px; width: 818px; }
  .section-title { font-size: 21px; font-weight: 400; color: var(--heading); padding-bottom: 6px; border-bottom: 1px solid var(--rule); white-space: nowrap; }
  .about p { font-size: 12.7px; line-height: 18.5px; color: var(--body-text); }
  .about .intro { margin-top: 14px; }
  .about .gap-lg { margin-top: 29px; }
  .about .gap-sm { margin-top: 6px; }

  .blog { position: absolute; left: 889px; top: 818px; width: 270px; }
  .post { margin-top: 14px; }
  .post + .post { margin-top: 24px; }
  .post-date { font-size: 14px; color: #333; }
  .post-title { font-size: 14px; color: var(--link); margin-top: 5px; }
  .post-text { font-size: 12.7px; line-height: 16px; color: #5a5a5a; margin-top: 7px; width: 240px; }
  .post-more { display: flex; align-items: center; gap: 6px; font-size: 13px; color: var(--link); margin-top: 10px; }

  .footer {
    position: absolute; left: 0; top: 1142px; width: 1182px; height: 58px;
    background: var(--footer); border-top: 3px solid #7fb1d3; color: var(--white);
  }
  .footer .copyright { position: absolute; left: 36px; top: 21px; font-size: 13px; white-space: nowrap; }
  .footer-nav { position: absolute; left: 855px; top: 23px; font-size: 13px; white-space: nowrap; }
  .footer-nav a { color: var(--white); }
  .footer-nav i { font-style: normal; margin: 0 6px; }
</style>
</head>
<body>
  <div class="top-strip"></div>

  <header>
    <a class="brand" href="#">
      <span class="brand-mark"></span>
      <span class="brand-name">Brovana</span>
    </a>
    <div class="contact-bar">
      <span>Get In Touch</span>
      <a class="social-box" href="#" aria-label="Social profile"></a>
      <a class="social-box" href="#" aria-label="Social profile"></a>
      <a class="social-box" href="#" aria-label="Social profile"></a>
    </div>
    <nav class="main-nav">
      <a href="#" style="width:104px">Main</a>
      <a href="#" style="width:174px">About Company</a>
      <a href="#" style="width:114px">Services</a>
      <a href="#" style="width:143px">Testimonials</a>
      <a href="#" style="width:89px">Blog</a>
      <a href="#" style="width:110px">Contact</a>
    </nav>
  </header>

  <section class="hero-band">
  </section>
  <div class="slider">
    <div class="slider-photo" role="img" aria-label="Photo of a doctor in a white coat holding a tablet computer with a stylus"></div>
    <div class="slider-copy">
      <h1 class="slider-title">Health &amp; IT Services</h1>
      <div class="slider-subline">HEALTH &amp; MEDICAL SUBLINE GOES HERE</div>
      <p class="slider-text">We like challenges and do complete these challenge with expertise we like solving questions that arises in such projects as these helps us to grow also.</p>
      <div class="slider-actions">
        <a class="btn btn-read" href="#">READ MORE&nbsp;&nbsp;›</a>
        <a class="btn btn-services" href="#">VIEW MORE SERVICES&nbsp;&nbsp;›</a>
      </div>
    </div>
  </div>
  <a class="slider-arrow prev" href="#" aria-label="Previous slide">
    <svg width="10" height="18" viewBox="0 0 10 18"><path d="M8 2 L2 9 L8 16" fill="none" stroke="#1a6fa8" stroke-width="1.6"/></svg>
  </a>
  <a class="slider-arrow next" href="#" aria-label="Next slide">
    <svg width="10" height="18" viewBox="0 0 10 18"><path d="M2 2 L8 9 L2 16" fill="none" stroke="#1a6fa8" stroke-width="1.6"/></svg>
  </a>

  <section class="services">
    <div class="service" style="left:11px">
      <div class="service-head">
        <svg width="32" height="32" viewBox="0 0 32 32"><path d="M11 2h10v9h9v10h-9v9H11v-9H2V11h9z" fill="#5cb82c"/></svg>
        <h3>Health Services</h3>
      </div>
      <p>We have learnt that designing is not only inclined to powerful imaginations but also focused and attractive to expected viewers also.</p>
      <a class="more" href="#">view <b>more..</b></a>
    </div>
    <div class="service-divider" style="left:271px"></div>
    <div class="service" style="left:294px">
      <div class="service-head">
        <svg width="38" height="42" viewBox="0 0 38 42"><rect x="3" y="2" width="32" height="24" rx="2" fill="#cfd6dc" stroke="#7d8790"/><rect x="6" y="5" width="26" height="18" fill="#2a7fc9"/><rect x="15" y="26" width="8" height="5" fill="#9aa3ab"/><rect x="2" y="31" width="34" height="9" rx="2" fill="#e3e7ea" stroke="#8b949c"/></svg>
        <h3>IT Services</h3>
      </div>
      <p>We have learnt that designing is not only inclined to powerful imaginations but also focused and attractive to expected viewers also.</p>
      <a class="more" href="#">view <b>more..</b></a>
    </div>
    <div class="service-divider" style="left:550px"></div>
    <div class="service" style="left:572px">
      <div class="service-head">
        <svg width="42" height="34" viewBox="0 0 42 34"><path d="M2 18 L9 12 L16 20 L34 2 L40 8 L16 32 Z" fill="#4fae2a" stroke="#2f7d16"/></svg>
        <h3>Other Services</h3>
      </div>
      <p>We have learnt that designing is not only inclined to powerful imaginations but also focused and attractive to expected viewers also.</p>
      <a class="more" href="#">view <b>more..</b></a>
    </div>
    <div class="service-divider" style="left:828px"></div>
    <div class="service" style="left:856px">
      <div class="service-head">
        <svg width="28" height="50" viewBox="0 0 28 50"><rect x="4" y="2" width="20" height="8" rx="2" fill="#e8e8e8" stroke="#a5a5a5"/><rect x="2" y="10" width="24" height="38" rx="4" fill="#f7f7f7" stroke="#b0b0b0"/><path d="M11 22h6v6h6v6h-6v6h-6v-6H5v-6h6z" fill="#d8282c"/></svg>
        <h3>Medical Services</h3>
      </div>
      <p>We have learnt that designing is not only inclined to powerful imaginations but also focused and attractive to expected viewers also.</p>
      <a class="more" href="#">view <b>more..</b></a>
    </div>
  </section>

  <div class="section-rule"></div>

  <section class="about">
    <h2 class="section-title">About Our Company</h2>
    <p class="intro">Brovana is an information technology incubator. We cultivate and groom start-ups from concept to reality to profitability. Brovana is managed and owned by entrepreneurs and technologists with proven start-up success. We seek to leverage synergies between our companies which foster innovation, stimulate creativity, increase productivity, streamline operational processes, and facilitate opportunity</p>
    <p class="gap-lg">Static website are the which are usually been used and are benefited through the Professionals and Small Companies. The companies with fewer budgets can promote their products and services through the static website and gain a lot.</p>
    <p class="gap-sm">&nbsp;To manage the static website HTML knowledge is the required. The simple website are also said as the static web as its embedded on a page.</p>
    <p class="gap-sm">Static website is a simple way to get your message out to the public. Static website are cheaper and also it needs less maintenance too. It’s the simplest, cheapest and also the basic thing the search engine picks it up very easily. We at Veltrano provide you the best simple websites too with total work done as using all the best designing and all done so that you can achieve the goal of yours through our work done on your website.</p>
  </section>

  <aside class="blog">
    <h2 class="section-title">Latest Blog &amp; News</h2>
    <article class="post">
      <div class="post-date">20.March.2012</div>
      <div class="post-title">News Headline goes here</div>
      <p class="post-text">Veltrano eSolutions to specialize in advanced projects and ongoing projects that require permanent support and maintenance.</p>
      <a class="post-more" href="#">READ MORE <svg width="7" height="10" viewBox="0 0 7 10"><path d="M1 1 L5 5 L1 9" fill="none" stroke="#1b7fc1" stroke-width="2"/></svg></a>
    </article>
    <article class="post">
      <div class="post-date">20.March.2012</div>
      <div class="post-title">News Headline goes here</div>
      <p class="post-text">Veltrano eSolutions to specialize in advanced projects and ongoing projects</p>
      <a class="post-more" href="#">READ MORE <svg width="7" height="10" viewBox="0 0 7 10"><path d="M1 1 L5 5 L1 9" fill="none" stroke="#1b7fc1" stroke-width="2"/></svg></a>
    </article>
  </aside>

  <footer class="footer">
    <div class="copyright">© 2012 Company Name &nbsp;|&nbsp; All right reserved</div>
    <nav class="footer-nav">
      <a href="#">Main</a><i>|</i><a href="#">About</a><i>|</i><a href="#">Services</a><i>|</i><a href="#">Testimonials</a><i>|</i><a href="#">Contact</a>
    </nav>
  </footer>
</body>
</html>
```